amber orchard fellowship non profit

I need a simple static website for a non-profit organization that includes blog capacity through Wordpress. The non-profit organization provides education and funding for alternative births and post natal care (doulas and mid-wives) for women. I have the domain name already but not the hosting. I've also set up a gmail account to link to the contact me page.
Updates

Also, would love warm colors.  Background can be white but toolbar and other accents could be peachy warm, tan / mauvish earthy colors.

Thanks.

Target Market(s)

The webstie will be for women who are going through the birthing process or have just given birth. Targeted toward women 16 to 50. The site will include various international outreach programs

Industry/Entity Type

Non Profit

Number of Pages Required

5+ pages

Requirements
Must have
• I want a site that I can control content after it has been designed. So I can add and change copy once it's up. It also must have photo and blog capacity (blog through Wordpress). Toolbar should include (with corresponding pages behind it that I will later include more info that I can update myself) Home, About, Resources / Links, Workshops, Members/Board, Donate Here-sponsors, Forum, International Outreach and somewhere on the homepage: Membership sign-up, Contact.
• The copy attached can be used on the home page.  Then where it explains about the founder, can be in the About section.

• Use warm tones - like peaches or mauvish earthy tan colors for the Toolbars.  (Background can be white.) 
• Use logo (attached) in banner on left and tagline: 
• Non-profit organization providing pre- and postnatal care for women.

• Would like the black and white photo with the mom's hands and baby's feet used as a constant photo and/or in the banner.
Nice to have
• Video capacity for me to add information.  This can be on the blog (through wordpress.)
Should not have
• No stiff, rigid lines.

```html
<!DOCTYPE html>
<html lang="en">
<head>
<meta charset="utf-8">
<title>Amber Orchard Fellowship</title>
<link rel="stylesheet" href="https://fonts.googleapis.com/css2?family=Arimo:wght@400;700&family=Didact+Gothic&family=Short+Stack&display=swap">
<style>
  :root {
    --backdrop: #efe8df;
    --paper: #ffffff;
    --tagline-red: #b00000;
    --tagline-red-dark: #8a0000;
    --hero-pink: #f9c6f6;
    --soft-pink: #f6d2f0;
    --brand-blue: #1f3f98;
    --ink: #1a1a1a;
    --muted: #5a5a5a;
    --accent-red: #a10c0c;
    --tag-cream: #fbf6cf;
    --rule: #555555;
  }
  * { box-sizing: border-box; margin: 0; padding: 0; }
  html, body { width: 1024px; height: 1200px; overflow: hidden; }
  body {
    position: relative;
    background: var(--backdrop);
    font-family: "Arimo", Arial, sans-serif;
    color: var(--ink);
  }
  .abs { position: absolute; }

  /* Tagline card */
  .tagline-card {
    left: 162px; top: 57px; width: 778px; height: 110px;
    background: var(--paper);
    box-shadow: 0 2px 8px rgba(0,0,0,.25);
  }
  .tagline-bar {
    left: 178px; top: 75px; width: 746px; height: 92px;
    background: linear-gradient(180deg, var(--tagline-red) 0%, var(--tagline-red-dark) 100%);
  }
  .tagline-text {
    left: 198px; top: 104px;
    font-family: "Short Stack", cursive;
    font-size: 15px; color: #ffe8e8; letter-spacing: .3px;
  }
  .header-icons { left: 852px; top: 87px; display: flex; gap: 18px; }

  /* Main page */
  .page {
    left: 50px; top: 151px; width: 924px; height: 1005px;
    background: linear-gradient(180deg, var(--paper) 0%, var(--paper) 65%, var(--soft-pink) 100%);
    box-shadow: 0 3px 12px rgba(0,0,0,.3);
  }
  .page-inner {
    left: 69px; top: 170px; width: 886px; height: 967px;
    background: linear-gradient(180deg, #ffffff 35%, #fbeaf7 75%, var(--soft-pink) 100%);
  }
  .hero { left: 69px; top: 170px; width: 886px; height: 341px; background: var(--hero-pink); }

  .brand { left: 145px; top: 318px; display: flex; align-items: center; gap: 10px; }
  .brand-dot { width: 22px; height: 22px; border-radius: 50%; background: var(--brand-blue); }
  .brand-name { font-family: "Arimo", Arial, sans-serif; font-weight: 700; font-size: 24px; color: var(--brand-blue); }

  .login { left: 145px; top: 415px; }
  .login-field {
    display: block; width: 186px; height: 24px; margin-bottom: 9px;
    border: 1px solid #8d8d8d; background: #fff;
    font-family: "Arimo", Arial, sans-serif; font-size: 12px; color: #555; padding: 4px 6px;
  }
  .login-button {
    left: 344px; top: 431px; width: 88px; height: 24px;
    background: #fff; transform: rotate(-2deg);
    box-shadow: 1px 2px 4px rgba(0,0,0,.2);
    font-family: "Short Stack", cursive; font-size: 13px; text-align: center; line-height: 24px;
  }
  .forgot { left: 148px; top: 483px; font-size: 10px; }
  .forgot a { color: var(--ink); }

  .hero-photo {
    left: 556px; top: 156px; width: 338px; height: 362px;
    transform: rotate(3deg);
    background: radial-gradient(ellipse at 50% 50%, #e58ae0 0%, #b154ad 30%, #111 70%);
    box-shadow: 2px 4px 10px rgba(0,0,0,.35);
  }

  /* Navigation tags */
  .nav { left: 80px; top: 535px; }
  .nav-tag {
    position: absolute; width: 176px; height: 32px;
    background: var(--tag-cream);
    box-shadow: 1px 2px 4px rgba(0,0,0,.25);
    font-size: 14px; letter-spacing: 1.5px; text-decoration: none; color: var(--ink);
    line-height: 32px; text-align: center;
  }
  .nav-divider { left: 285px; top: 536px; height: 288px; border-left: 1px dashed var(--rule); }

  /* Welcome */
  .welcome-title {
    left: 322px; top: 544px; width: 454px;
    font-family: "Didact Gothic", sans-serif; font-size: 40px; color: var(--muted);
    border-bottom: 1px solid #9a9a9a; line-height: 41px;
  }
  .welcome-lead {
    left: 322px; top: 603px; width: 440px;
    font-size: 14px; line-height: 24px; color: var(--accent-red);
  }
  .welcome-body {
    left: 322px; top: 664px; width: 455px;
    font-size: 12px; line-height: 24px; color: var(--ink);
  }
  .side-photo {
    left: 800px; top: 548px; width: 140px; height: 158px;
    transform: rotate(8deg);
    background: linear-gradient(160deg, #6b4a2e 0%, #b07a45 55%, #2a1f17 100%);
    border: 4px solid #fff;
    box-shadow: 2px 3px 6px rgba(0,0,0,.3);
  }

  /* Calls to action */
  .cta-rule { left: 112px; top: 860px; width: 804px; border-top: 1px dashed var(--rule); }
  .cta { top: 872px; display: flex; align-items: center; gap: 10px; }
  .cta-title { font-size: 24px; color: var(--ink); }
  .cta-sub { font-size: 14px; }

  /* Feature cards */
  .feature { top: 925px; width: 232px; text-align: center; }
  .feature-photo {
    width: 232px; height: 128px; border: 6px solid #fff;
    box-shadow: 0 1px 4px rgba(0,0,0,.2);
  }
  .feature-title { margin-top: 14px; font-size: 16px; font-weight: 700; letter-spacing: .5px; }
  .feature-text { margin-top: 3px; font-size: 10px; line-height: 13px; }
  .feature-divider { top: 926px; height: 192px; border-left: 1px dashed var(--rule); }
</style>
</head>
<body>

  <div class="abs tagline-card"></div>
  <header>
    <div class="abs tagline-bar"></div>
    <p class="abs tagline-text">Non-profit organization providing pre &amp; postnatal care for women</p>
    <div class="abs header-icons">
      <svg width="16" height="12" viewBox="0 0 16 12" aria-label="Email"><rect x=".5" y=".5" width="15" height="11" fill="none" stroke="#fff"/><path d="M.5 .5 8 7l7.5-6.5" fill="none" stroke="#fff"/></svg>
      <svg width="16" height="14" viewBox="0 0 16 14" aria-label="Home"><path d="M1 7 8 1l7 6M3 6v7h10V6" fill="none" stroke="#fff"/><rect x="6.5" y="9" width="3" height="4" fill="none" stroke="#fff"/></svg>
    </div>
  </header>

  <main>
    <div class="abs page"></div>
    <div class="abs page-inner"></div>

    <section class="abs hero"></section>
    <div class="abs brand">
      <span class="brand-dot"></span>
      <span class="brand-name">Amber Orchard Fellowship</span>
    </div>

    <form class="abs login">
      <input class="login-field" type="text" value="Username" aria-label="Username">
      <input class="login-field" type="password" value="***********" aria-label="Password">
    </form>
    <div class="abs login-button">LOGIN</div>
    <p class="abs forgot">Forgot username? <a href="#">Click here</a></p>

    <div class="abs hero-photo" role="img" aria-label="Black and white photo of a mother's hands forming a heart around baby feet, tinted pink"></div>

    <nav class="abs nav">
      <a class="nav-tag" href="#" style="left:2px;top:0;transform:rotate(-1deg)">ABOUT</a>
      <a class="nav-tag" href="#" style="left:6px;top:47px;transform:rotate(1deg)">RESOURCES</a>
      <a class="nav-tag" href="#" style="left:2px;top:95px;transform:rotate(-.5deg)">WORKSHOPS</a>
      <a class="nav-tag" href="#" style="left:7px;top:139px;transform:rotate(.5deg)">FORUM</a>
      <a class="nav-tag" href="#" style="left:0;top:188px;transform:rotate(1deg)">BOARD</a>
    </nav>
    <div class="abs nav-divider"></div>

    <h1 class="abs welcome-title">welcome</h1>
    <p class="abs welcome-lead">Help us help our sisters and daughters to take back control over how we bring the next generation to life</p>
    <p class="abs welcome-body">Phasellus ut placerat risus. Fusce a erat massa. Curabitur sapien massa, tempus euismod aliquam vitae, bibendum ac dui. Class aptent taciti sociosqu ad litora torquent per conubia nostra, per inceptos himenaeos. Aliquam erat volutpat. Pellentesque elementum leo in purus eleifend at iaculis quam commodo. Nulla ante lorem, convallis vel auctor ut, fermentum nec ante. Donec viverra consequat lacus, non sodales nibh suscipit vel. Quisque sagittis velit nec mi placerat suscipit. Nam tincidunt pharetra congue.</p>
    <div class="abs side-photo" role="img" aria-label="Photo of a pregnant woman holding her belly"></div>

    <div class="abs cta-rule"></div>
    <div class="abs cta" style="left:112px">
      <svg width="28" height="22" viewBox="0 0 28 22" aria-hidden="true"><path d="M0 0 28 11 0 22 7 11Z" fill="var(--accent-red)"/></svg>
      <span class="cta-title">Join here,</span><span class="cta-sub">free membership and newsletter</span>
    </div>
    <div class="abs cta" style="left:628px">
      <svg width="28" height="22" viewBox="0 0 28 22" aria-hidden="true"><path d="M0 0 28 11 0 22 7 11Z" fill="var(--accent-red)"/></svg>
      <span class="cta-title">Donate here,</span><span class="cta-sub">for a good cause</span>
    </div>

    <article class="abs feature" style="left:98px">
      <div class="feature-photo" role="img" aria-label="Photo of a mother and daughter playing outdoors under a blue sky" style="background:linear-gradient(180deg,#6fa7e6 0%,#b9d6f2 60%,#c44a2b 100%)"></div>
      <h2 class="feature-title">INTERNATIONAL OUTREACH</h2>
      <p class="feature-text">Adopt/create a healthcare facility overseas</p>
    </article>
    <div class="abs feature-divider" style="left:363px"></div>
    <article class="abs feature" style="left:397px">
      <div class="feature-photo" role="img" aria-label="Photo of a newborn's tiny hand holding a parent's fingers" style="background:linear-gradient(135deg,#8a6a5e 0%,#e8c8bc 50%,#f3ddd3 100%)"></div>
      <h2 class="feature-title">VOLUNTEERS</h2>
      <p class="feature-text">Doulas, baby sitters, insurance, legal experts, musicians' soothing music, meditations, yogis</p>
    </article>
    <div class="abs feature-divider" style="left:659px"></div>
    <article class="abs feature" style="left:692px">
      <div class="feature-photo" role="img" aria-label="Photo of a toddler leaning against a pregnant belly" style="background:linear-gradient(90deg,#d8b89a 0%,#efdccb 50%,#8a8a8a 100%)"></div>
      <h2 class="feature-title">EVENTS &amp; NEWS</h2>
      <p class="feature-text">Latest updates &amp; information from around the world</p>
    </article>
  </main>

</body>
</html>
```